Willowbrook Body Care business is seeking a Business Card Design

We are a new natural therapy business that needs a Business Card Design with an appointment card on the back.

We offer Myotherapy (muscle therapy) services and have a strong focus and commitment to helping people relieve pain and restore movement to their bodies.

I am attaching my business logo for you information.

Business card must contain my logo and have space for name, title, qualifications, phone number, email, web address

Appointment Card on the back of the card must contain space to write next appointment date, time and name of therapist and cancellation policy.

Cancellation Policy
Minimum of 24hrs notice is required prior to appointment time or full treatment fees with apply.

Industry/Entity Type

Business

```html
<!DOCTYPE html>
<html lang="en">
<head>
<meta charset="utf-8">
<title>Willowbrook Body Care – Business &amp; Appointment Card</title>
<link href="https://fonts.googleapis.com/css2?family=Open+Sans:wght@400;600&family=Libre+Baskerville:wght@400;700&display=swap" rel="stylesheet">
<style>
  :root {
    --brand-red: #bf1e2e;
    --brand-brown: #574a41;
    --brand-green: #7fba3a;
    --ink: #4a3f38;
    --card-white: #ffffff;
    --backdrop-light: #dcdcdc;
    --backdrop-dark: #a9a9a9;
  }
  * { box-sizing: border-box; margin: 0; padding: 0; }
  html, body { width: 1200px; height: 1000px; overflow: hidden; }
  body {
    background: radial-gradient(ellipse at 40% 40%, var(--backdrop-light), var(--backdrop-dark));
    position: relative;
    font-family: "Open Sans", sans-serif;
  }
  .card {
    position: absolute;
    background: var(--card-white);
    box-shadow: 0 14px 30px rgba(0,0,0,0.22);
    overflow: hidden;
  }

  /* Front: business card */
  .card--front { left: 120px; top: 40px; width: 750px; height: 440px; }
  .brand { position: absolute; left: 32px; top: 62px; display: flex; align-items: center; gap: 14px; }
  .brand__square { width: 58px; height: 58px; background: var(--brand-red); }
  .brand__name { font-weight: 600; font-size: 30px; color: var(--brand-red); line-height: 1; }
  .brand__tagline { position: absolute; left: 104px; top: 132px; font-size: 15px; color: var(--brand-green); }

  .person { position: absolute; left: 0; width: 300px; top: 270px; text-align: center; font-family: "Libre Baskerville", serif; }
  .person__name { font-weight: 700; font-size: 27px; color: var(--brand-red); }
  .person__title { font-size: 22px; color: var(--ink); margin-top: 8px; }

  .divider { position: absolute; left: 300px; top: 238px; width: 3px; height: 140px; background: var(--brand-brown); }

  .contacts { position: absolute; left: 352px; top: 252px; list-style: none; font-family: "Libre Baskerville", serif; font-size: 22px; color: var(--ink); }
  .contacts li { display: flex; align-items: center; gap: 12px; height: 38px; }
  .contacts svg { width: 28px; height: 28px; flex: none; }

  .color-bar { position: absolute; left: 0; bottom: 0; width: 100%; height: 22px; display: flex; }
  .color-bar span { flex: 1; }
  .color-bar .red { background: var(--brand-red); }
  .color-bar .brown { background: var(--brand-brown); }
  .color-bar .green { background: var(--brand-green); }

  /* Back: appointment card */
  .card--back { left: 360px; top: 500px; width: 730px; height: 450px; }
  .appt__header { height: 86px; background: var(--brand-red); color: var(--card-white); font-weight: 600; font-size: 34px; display: flex; align-items: center; justify-content: center; }
  .appt__fields { padding: 40px 36px 0 46px; list-style: none; }
  .appt__fields li { display: flex; align-items: flex-end; gap: 10px; height: 76px; font-size: 23px; color: var(--ink); }
  .appt__fields .line { flex: 1; border-bottom: 2px solid var(--brand-brown); margin-bottom: 8px; }
  .policy { position: absolute; left: 66px; top: 350px; right: 30px; color: var(--brand-red); font-size: 18px; line-height: 1.15; }
  .policy__title { font-weight: 600; }
</style>
</head>
<body>

<section class="card card--front" aria-label="Business card front">
  <div class="brand">
    <div class="brand__square"></div>
    <div class="brand__name">Willowbrook Body Care</div>
  </div>
  <div class="brand__tagline">Natural Muscle Health</div>

  <div class="person">
    <div class="person__name">CLARA DUNMORE</div>
    <div class="person__title">Therapist</div>
  </div>

  <div class="divider"></div>

  <ul class="contacts">
    <li>
      <svg viewBox="0 0 28 28" aria-hidden="true"><rect width="28" height="28" fill="#bf1e2e"/><path d="M8 6c1-1 2-1 3 0l2 3c.5 1 0 2-1 2.5 1 2 2.5 3.5 4.5 4.5.5-1 1.5-1.5 2.5-1l3 2c1 1 1 2 0 3l-1.5 1.5C17 22 7 12 6.5 7.5z" fill="#fff"/></svg>
      000-987-654
    </li>
    <li>
      <svg viewBox="0 0 28 28" aria-hidden="true"><rect width="28" height="28" fill="#bf1e2e"/><rect x="5" y="8" width="18" height="13" fill="none" stroke="#fff" stroke-width="2"/><path d="M5 8l9 7 9-7" fill="none" stroke="#fff" stroke-width="2"/></svg>
      hello@willowbrookcare.com
    </li>
    <li>
      <svg viewBox="0 0 28 28" aria-hidden="true"><rect width="28" height="28" fill="#bf1e2e"/><g fill="none" stroke="#fff" stroke-width="1.6"><circle cx="14" cy="14" r="8"/><ellipse cx="14" cy="14" rx="3.5" ry="8"/><path d="M6 14h16M7.5 10h13M7.5 18h13"/></g></svg>
      www.willowbrookcare.com
    </li>
  </ul>

  <div class="color-bar"><span class="red"></span><span class="brown"></span><span class="green"></span></div>
</section>

<section class="card card--back" aria-label="Appointment card back">
  <div class="appt__header">YOUR APPOINTMENT</div>
  <ul class="appt__fields">
    <li>Appointment Date: <span class="line"></span></li>
    <li>Appointment Time: <span class="line"></span></li>
    <li>Name of Therapist: <span class="line"></span></li>
  </ul>
  <div class="policy">
    <div class="policy__title">Cancellation Policy</div>
    <div>Minimum of 24hrs notice is required prior to appointment time or full treatment fees will apply</div>
  </div>
</section>

</body>
</html>
```